Brindlequest.com is a mountain biking and climbing travel company. We need a advertisement fo...

We need a advertisement for the back cover of a guide book. We would like a simple but strong ad that includes our logo. It must state that we are a biking and climbing company and people can contact us at the web site brindlequest.com We would like you to incorparate and below photo and logo on the ad.

```html
<!DOCTYPE html>
<html lang="en">
<head>
<meta charset="utf-8">
<title>Brindlequest Tours – Back Cover Advertisement</title>
<link rel="stylesheet" href="https://fonts.googleapis.com/css2?family=Michroma&family=Montserrat:wght@500;600;700&display=swap">
<style>
  :root {
    --stage: #3b3b3b;
    --ink: #0b0b0b;
    --white: #ffffff;
    --amber: #e9a63b;
    --photo-sky: #3f5a33;
    --photo-wall: #c9b9a4;
    --photo-street: #6f6d6c;
  }
  * { margin: 0; padding: 0; box-sizing: border-box; }
  html, body { width: 1200px; height: 675px; overflow: hidden; background: var(--stage); }
  .canvas { position: relative; width: 1200px; height: 675px; }

  .ad {
    position: absolute; left: 380px; top: 26px;
    width: 440px; height: 622px;
    overflow: hidden; background: var(--ink);
  }
  .ad__photo {
    position: absolute; left: 0; top: 0; width: 440px; height: 510px;
    background:
      radial-gradient(ellipse 90px 120px at 200px 220px, rgba(217,146,58,.7), transparent 70%),
      linear-gradient(180deg, var(--photo-sky) 0%, var(--photo-wall) 22%, #b69a86 45%, var(--photo-street) 70%, #585858 100%);
  }
  .ad__tear { position: absolute; left: 0; top: 470px; width: 440px; height: 48px; }

  .ad__cyclist {
    position: absolute; left: 10px; top: 376px; width: 110px; height: 114px;
    background: radial-gradient(ellipse at 50% 55%, rgba(20,20,20,.75) 0%, rgba(20,20,20,.35) 50%, transparent 72%);
  }
  .ad__climber {
    position: absolute; left: 300px; top: 360px; width: 140px; height: 114px;
    background: radial-gradient(ellipse at 55% 50%, rgba(233,166,59,.7) 0%, rgba(233,166,59,.3) 50%, transparent 72%);
  }
  .ad__rope { position: absolute; left: 364px; top: 0; width: 2px; height: 548px; background: var(--amber); }

  .headline {
    position: absolute; left: 0; width: 440px; text-align: center;
    font-family: 'Michroma', sans-serif; line-height: 1;
  }
  .headline--name { top: 324px; font-size: 29px; color: var(--white); letter-spacing: -0.5px; }
  .headline--tours { top: 360px; font-size: 33px; color: var(--amber); left: -5px; }

  .tagline {
    position: absolute; left: 0; top: 411px; width: 440px; text-align: center;
    font-family: 'Montserrat', sans-serif; font-weight: 600; font-size: 14px;
    color: var(--white); letter-spacing: .3px;
  }
  .cta {
    position: absolute; left: 162px; top: 435px; width: 110px; height: 25px;
    background: var(--amber); color: var(--white);
    font-family: 'Montserrat', sans-serif; font-weight: 600; font-size: 8.5px;
    display: flex; align-items: center; justify-content: center; letter-spacing: .2px;
  }

  .brand {
    position: absolute; left: 0; top: 530px; width: 440px;
    display: flex; align-items: center; justify-content: center; gap: 12px;
  }
  .brand__mark { width: 34px; height: 34px; border-radius: 50%; background: var(--white); }
  .brand__name { font-family: 'Michroma', sans-serif; font-size: 23px; color: var(--white); }
  .web {
    position: absolute; left: 0; top: 597px; width: 440px; text-align: center;
    font-family: 'Montserrat', sans-serif; font-weight: 500; font-size: 8.5px;
    letter-spacing: 2.4px; color: var(--white);
  }
</style>
</head>
<body>
<div class="canvas">
  <section class="ad" aria-label="Brindlequest Tours advertisement">
    <div class="ad__photo" role="img" aria-label="Photograph of a narrow evening street in an old hillside town with lit shop windows and passers-by"></div>
    <div class="ad__cyclist" role="img" aria-label="Silhouette of a mountain biker riding"></div>
    <div class="ad__climber" role="img" aria-label="Amber silhouette of a climber abseiling on the rope"></div>

    <svg class="ad__tear" viewBox="0 0 440 48" preserveAspectRatio="none" aria-hidden="true">
      <path d="M0 22 L30 18 L55 24 L90 16 L120 21 L150 15 L185 20 L215 12 L250 16 L280 9 L310 13 L345 7 L375 11 L405 5 L440 8 L440 48 L0 48 Z" fill="#0b0b0b"/>
    </svg>

    <div class="ad__rope"></div>

    <h1 class="headline headline--name">BRINDLEQUEST</h1>
    <h2 class="headline headline--tours">TOURS</h2>
    <p class="tagline">CLIMBING + RIDING</p>
    <div class="cta">BOOK TOUR NOW</div>

    <div class="brand">
      <span class="brand__mark"></span>
      <span class="brand__name">Brindlequest</span>
    </div>
    <p class="web">www.brindlequest.com</p>
  </section>
</div>
</body>
</html>
```